Trade Show Poster/Booth Backdrop for Rugged Technology Business

I need a graphic design for an 8' x 6' poster to hang on back wall of my event booth. Design must be consistent with my company's colors, logo, and current branding as shown on website, plain circle, and plain circle (links provided). You can propose other elements, but there are certain core images and text elements that must be incorporated. Print specifications also provided. File must be delivered on time and upload-ready.

Font styles to use
Sans Serif

Colors
33a6d7
0355a3
33b8a4
00a990
9bcb3b
abd036
cadf82
85cae6
86cfc6

Requirements
Nice to have
• Regarding color, I'm okay with designs using the orange version of the Morvex logo.
• Regarding the images I provided as potential background layers, I especially like the ones with rocky island profiles and exposed cliff faces. In addition to being a nice match color wise, they are subtle suggestions of ruggedness and working with technology that can handle extreme environments (which is a big part of the messaging focus).
Should not have
• Vibrant coloration is very much desired and OK, but please avoid a blend that goes to either extreme. For instance, too much dark blue makes it look like every other tech company ever. Too much warm, light green (other than for contrast elements) makes it look too tropical and casual.

```html
<!DOCTYPE html>
<html lang="en">
<head>
<meta charset="utf-8">
<title>Rugged Technology Solutions – Booth Backdrop</title>
<link rel="stylesheet" href="https://fonts.googleapis.com/css2?family=Arimo:wght@400;700&display=swap">
<style>
  :root {
    --deep-blue: #27479a;
    --ocean-teal: #1a8f8a;
    --forest-green: #1e9a4a;
    --bright-green: #2fae4e;
    --lime: #9bcb3b;
    --lime-light: #abd036;
    --sky: #85cae6;
    --brand-blue: #33a6d7;
    --brand-green: #3aa335;
    --navy: #1d5aa8;
    --white: #ffffff;
  }
  * { margin: 0; padding: 0; box-sizing: border-box; }
  html, body { width: 1200px; height: 900px; overflow: hidden; background: var(--white); }
  .backdrop {
    position: relative;
    width: 1200px;
    height: 900px;
    overflow: hidden;
    font-family: "Arimo", Arial, sans-serif;
  }
  .scene {
    position: absolute;
    inset: 0;
    background:
      radial-gradient(ellipse at 75% 55%, rgba(20, 110, 50, 0.55), transparent 60%),
      linear-gradient(100deg, var(--deep-blue) 0%, var(--ocean-teal) 38%, var(--forest-green) 70%, var(--bright-green) 100%);
  }
  .wave { position: absolute; inset: 0; width: 1200px; height: 900px; }
  .partners {
    position: absolute;
    top: 40px;
    left: 770px;
    display: flex;
    align-items: center;
    height: 116px;
    color: var(--white);
  }
  .partner-name { font-size: 52px; font-weight: 700; letter-spacing: -1px; }
  .partner-divider { width: 3px; height: 116px; background: var(--white); margin: 0 22px; }
  .partner-second { display: flex; align-items: center; gap: 12px; }
  .partner-dot { width: 22px; height: 22px; border-radius: 50%; background: var(--white); }
  .partner-second .partner-name { font-size: 44px; }
  .headline {
    position: absolute;
    top: 168px;
    left: 100px;
    color: var(--white);
    font-size: 60px;
    font-weight: 700;
    line-height: 72px;
    letter-spacing: 1px;
    text-shadow: 2px 3px 6px rgba(0, 0, 0, 0.45);
  }
  .services {
    position: absolute;
    top: 460px;
    left: 100px;
    color: var(--sky);
    font-size: 21px;
    font-weight: 700;
    line-height: 30px;
    letter-spacing: 0.5px;
  }
  .company {
    position: absolute;
    top: 780px;
    left: 872px;
    display: flex;
    align-items: center;
    gap: 14px;
  }
  .company-mark { width: 40px; height: 40px; border-radius: 50%; background: var(--brand-blue); }
  .company-name { color: var(--brand-green); font-size: 32px; font-weight: 400; line-height: 40px; }
  .social {
    position: absolute;
    left: 50px;
    top: 823px;
    display: flex;
    align-items: center;
    gap: 12px;
  }
  .social-dot { width: 46px; height: 46px; border-radius: 50%; background: var(--navy); }
  .social-handle { margin-left: 8px; color: var(--navy); font-size: 22px; font-weight: 400; }
</style>
</head>
<body>
<main class="backdrop">
  <div class="scene" role="img" aria-label="Photograph of a rugged forested island coastline with a calm bay, tinted from blue to green"></div>

  <svg class="wave" viewBox="0 0 1200 900" aria-hidden="true">
    <path fill="var(--lime)" d="M0,785 C200,795 400,758 600,690 C800,622 1000,585 1200,588 L1200,612 C1000,602 800,648 600,718 C400,786 200,822 0,805 Z"/>
    <path fill="var(--white)" d="M0,805 C200,822 400,786 600,718 C800,648 1000,602 1200,612 L1200,900 L0,900 Z"/>
    <path fill="var(--lime-light)" d="M255,600 C135,592 42,650 45,722 C48,782 108,812 172,806 C112,790 82,745 96,700 C116,640 182,610 255,600 Z"/>
  </svg>

  <div class="partners">
    <span class="partner-name">Morvex</span>
    <span class="partner-divider"></span>
    <span class="partner-second">
      <span class="partner-dot"></span>
      <span class="partner-name">Halvo</span>
    </span>
  </div>

  <h1 class="headline">FULLY RUGGED<br>&amp; BUSINESS CLASS<br>TECHNOLOGY<br>SOLUTIONS</h1>

  <p class="services">MOBILITY. COMPUTING. MOUNTING<br>PRINTING. IMAGING. STORAGE</p>

  <div class="company">
    <span class="company-mark"></span>
    <span class="company-name">Talven Group</span>
  </div>

  <div class="social">
    <span class="social-dot"></span>
    <span class="social-dot"></span>
    <span class="social-handle">@TalvenGroupIT</span>
  </div>
</main>
</body>
</html>
```